Natural cosmetics company is looking for a designer to produce the labels of the products and

Hello, Nus need a label and logo design for our brand LW FERNMIRA. It is a brand specializing in the sale of 100% Natural cosmetic products on the internet. The first range is based on snail slime. I am looking for a clean design in green tones. The final design must be forwarded to the supplier for printing and shipping of the products. I realized a first idea for a logo, but I am interested in other ideas / suggestions. You have carte blanche :)
Here are the rules to follow for sending labels to the supplier:
• Sizes:
- Airless bottle: 10.3 x 5.5 cm
- Jar: 20x2.5cm
• Files must be in Corel Draw (. cdr) and / or vector PDF format
You must attach the file of the fonts used for the text in the label - We need this file as many fonts are difficult to find and we might need to move some text around for printing purposes
• The logo of your brand must be in a vector format along with all other components.
• Please do not add any borders or any cut marks to the design. We will do it on our end as we need to follow specific indications with our printing suppliers.
• All text and graphics must be at least 6mm from the edge
• The dimensions indicated by us must be respected in the overall size of the label
• The resolution to be used should be 300 cpi and in CMYK
• The text size should be readable and at least 4.5 points.

```html
<!DOCTYPE html>
<html lang="en">
<head>
<meta charset="utf-8">
<title>LW Fernmira – Snail Slime Regenerating Serum Labels</title>
<link rel="stylesheet" href="https://fonts.googleapis.com/css2?family=Kreon:wght@300;400;600&family=Kaushan+Script&family=Kalam:wght@400&display=swap">
<style>
  :root {
    --backdrop: #d7e49b;
    --label-paper: #ffffff;
    --pattern-tint: #f3f7e2;
    --leaf-green: #1f9a3e;
    --ink: #2b2b2b;
    --ink-soft: #4a4a4a;
    --brush-black: #1c1c1c;
  }
  * { box-sizing: border-box; margin: 0; padding: 0; }
  html, body {
    width: 1200px;
    height: 486px;
    overflow: hidden;
    background: var(--backdrop);
  }
  .canvas {
    position: relative;
    width: 1200px;
    height: 486px;
    background: var(--backdrop);
    font-family: "Kreon", Georgia, serif;
    color: var(--ink);
  }

  /* Brand mark */
  .brand-mark {
    position: absolute;
    left: 32px;
    top: 203px;
    width: 228px;
    height: 228px;
    border-radius: 50%;
    background: var(--label-paper);
    border: 10px solid var(--brush-black);
    display: flex;
    align-items: center;
    justify-content: center;
  }
  .brand-mark__name {
    font-family: "Kreon", Georgia, serif;
    font-weight: 600;
    font-size: 30px;
    line-height: 1.1;
    text-align: center;
    color: var(--leaf-green);
  }

  /* Labels */
  .label {
    position: absolute;
    background: var(--label-paper);
    overflow: hidden;
  }
  .label__pattern {
    position: absolute;
    inset: 0;
    background: radial-gradient(circle at 50% 50%, var(--label-paper) 30%, var(--pattern-tint) 100%);
  }
  .label--jar { left: 76px; top: 71px; width: 791px; height: 98px; }
  .label--bottle { left: 294px; top: 201px; width: 407px; height: 217px; }

  .label__copy,
  .label__fineprint {
    position: absolute;
    white-space: nowrap;
    font-weight: 300;
  }
  .label__copy { color: var(--ink); }
  .label__fineprint { color: var(--ink-soft); }
  .label__copy-title { font-weight: 600; }

  .label__brand {
    position: absolute;
    border-radius: 50%;
    border: 2px solid var(--brush-black);
    display: flex;
    align-items: center;
    justify-content: center;
    text-align: center;
    font-family: "Kreon", Georgia, serif;
    font-weight: 600;
    color: var(--leaf-green);
    line-height: 1.05;
  }
  .label__product {
    position: absolute;
    font-family: "Kaushan Script", cursive;
    color: var(--leaf-green);
    white-space: nowrap;
    line-height: 1;
  }
  .label__rule {
    position: absolute;
    background: var(--leaf-green);
  }
  .label__range,
  .label__claim {
    position: absolute;
    white-space: nowrap;
    text-align: center;
    line-height: 1;
  }
  .label__range {
    font-family: "Kreon", Georgia, serif;
    font-weight: 400;
    color: var(--ink);
  }
  .label__claim {
    font-family: "Kalam", cursive;
    color: var(--brush-black);
  }

  /* Jar label placement */
  .label--jar .label__copy { left: 53px; top: 17px; font-size: 8.3px; line-height: 8.4px; }
  .label--jar .label__brand { left: 322px; top: 22px; width: 50px; height: 50px; font-size: 8px; }
  .label--jar .label__product { left: 387px; top: 17px; font-size: 24px; }
  .label--jar .label__rule { left: 382px; top: 45px; width: 121px; height: 2px; }
  .label--jar .label__range { left: 382px; top: 49px; width: 121px; font-size: 10.5px; }
  .label--jar .label__claim { left: 382px; top: 63px; width: 121px; font-size: 12px; }
  .label--jar .label__fineprint { left: 588px; top: 21px; font-size: 6.6px; line-height: 7px; }

  /* Bottle label placement */
  .label--bottle .label__copy { left: 27px; top: 30px; font-size: 8.4px; line-height: 8.4px; }
  .label--bottle .label__brand { left: 183px; top: 34px; width: 50px; height: 50px; font-size: 8.4px; }
  .label--bottle .label__product { left: 131px; top: 95px; font-size: 31px; }
  .label--bottle .label__rule { left: 163px; top: 133px; width: 119px; height: 3px; }
  .label--bottle .label__range { left: 126px; top: 140px; width: 160px; font-size: 13.6px; }
  .label--bottle .label__claim { left: 126px; top: 164px; width: 160px; font-size: 16px; }
  .label--bottle .label__fineprint { left: 318px; top: 34px; font-size: 6.6px; line-height: 7px; }
</style>
</head>
<body>
<main class="canvas">

  <div class="brand-mark">
    <span class="brand-mark__name">LW<br>Fernmira</span>
  </div>

  <section class="label label--jar" aria-label="Jar label">
    <div class="label__pattern" role="img" aria-label="Faint repeating pale green snail pattern"></div>
    <p class="label__copy">
      <span class="label__copy-title">Natural active ingredients in slime</span><br>
      Pure snail slime contains active ingredients<br>
      beneficial to the skin: allantoin, collagen,<br>
      glycolic acid, elastin, vitamin A and vitamin C,<br>
      natural antibiotic peptides. It is these<br>
      components that improve skin texture, help<br>
      heal skin lesions and restore radiance to the<br>
      complexion.
    </p>
    <div class="label__brand">LW<br>Fernmira</div>
    <div class="label__product">Snail Slime</div>
    <div class="label__rule"></div>
    <div class="label__range">Regenerating Serum</div>
    <div class="label__claim">100% Natural</div>
    <p class="label__fineprint">
      IpsumLorem Ipsumpsumcontains active<br>
      ingredients Lorem Ipsum psumcontains active<br>
      ingredients&nbsp; Lorem IpsumLorempsumcontains<br>
      active ingredientsIpsumLorem Ipsum<br>
      Lorem Ipsumcontains active ingredients beneficial<br>
      to the skin: allantoin, collagen, glycolic acid,<br>
      elastin, vitamin A andnatural antibiotic<br>
      Lorem Ipsumcontains active ingredients beneficial
    </p>
  </section>

  <section class="label label--bottle" aria-label="Airless bottle label">
    <div class="label__pattern" role="img" aria-label="Faint repeating pale green snail pattern"></div>
    <p class="label__copy">
      <span class="label__copy-title">Natural active</span><br>
      <span class="label__copy-title">ingredients in slime</span><br>
      Pure snail slime<br>
      contains active<br>
      ingredients<br>
      beneficial to the<br>
      skin: allantoin,<br>
      collagen, glycolic<br>
      acid, elastin, vitamin<br>
      A and vitamin C,<br>
      natural antibiotic<br>
      peptides. It is these<br>
      components that<br>
      improve skin<br>
      texture, help heal<br>
      skin lesions and<br>
      restore radiance to<br>
      the complexion.
    </p>
    <div class="label__brand">LW<br>Fernmira</div>
    <div class="label__product">Snail Slime</div>
    <div class="label__rule"></div>
    <div class="label__range">Regenerating Serum</div>
    <div class="label__claim">100% Natural</div>
    <p class="label__fineprint">
      Lorem Ipsum<br>
      Lorem<br>
      Ipsum Lorem<br>
      IpsumLorem<br>
      Ipsum<br>
      Lorem Ipsum<br>
      Lorem<br>
      IpsumLorem<br>
      IpsumLorem<br>
      Ipsum<br>
      Lorem<br>
      Ipsumcontains<br>
      active<br>
      ingredients<br>
      beneficial to the<br>
      skin: allantoin,<br>
      collagen, glycolic<br>
      acid, elastin,<br>
      vitamin A<br>
      andnatural<br>
      antibiotic
    </p>
  </section>

</main>
</body>
</html>
```